I need a new business card design for my pharmacy.

I need a business card design. I will include my logo.
The card needs to be readable. I prefer to have my logo on one side along with my website, the other side includes the other information. Please use combination of black, neon green, white, and silver. This needs to catch the eye but yet be clearly visible and legible. Thanks

Industry/Entity Type

Pharmacy

Contact Information for Business Card

It needs to have the following information listed:
Mel's Apothecary Owner/Pharm D.
7134 North Brook Lane
Sioux Falls, SD 57231
Phone 605-318-6207
Fax 605-318-6209
email: mel@melsapothecary-example.com
www.melsapothecary-example.com
Store hours Monday-Friday 8 am- 7 pm
Saturday 8 am- 12 pm
Sunday Closed
Please utilize the colors black, white, and neon green, maybe silver.

Requirements
Must have
• It needs to be easily readable!
Nice to have
• It should catch the eye.
Should not have
• Do not use any other colors except listed: black, neon green, white, & silver.

```html
<!DOCTYPE html>
<html lang="en">
<head>
<meta charset="utf-8">
<title>Mel's Apothecary – Business Card</title>
<link rel="stylesheet" href="https://fonts.googleapis.com/css2?family=Noto+Serif:ital,wght@0,700;1,400&family=PT+Sans+Narrow&display=swap">
<style>
  :root {
    --neon-green: #a8cd3a;
    --silver: #c0c0c0;
    --black: #000000;
    --text-light: #d2d2d2;
    --page: #ffffff;
  }
  html, body {
    margin: 0;
    padding: 0;
    width: 1200px;
    height: 1000px;
    overflow: hidden;
    background: var(--page);
  }
  .card {
    position: absolute;
    left: 46px;
    top: 63px;
    width: 1108px;
    height: 868px;
    background: var(--black);
    overflow: hidden;
  }
  .header-band {
    position: absolute;
    left: 0; top: 0;
    width: 100%;
    height: 117px;
    background: var(--neon-green);
  }
  .header-rule {
    position: absolute;
    left: 0; top: 117px;
    width: 100%;
    height: 21px;
    background: var(--silver);
  }
  .title-box {
    position: absolute;
    left: 101px; top: 9px;
    width: 897px;
    height: 98px;
    background: var(--black);
    display: flex;
    align-items: center;
    justify-content: center;
  }
  .title {
    margin: 0;
    flex: none;
    white-space: nowrap;
    font-family: "Noto Serif", serif;
    font-weight: 700;
    font-size: 50px;
    line-height: 1;
    color: var(--neon-green);
    transform: scaleX(0.76);
    transform-origin: center;
  }
  .info-line {
    position: absolute;
    margin: 0;
    font-family: "Noto Serif", serif;
    font-style: italic;
    font-weight: 400;
    font-size: 42px;
    line-height: 1;
    color: var(--text-light);
    white-space: nowrap;
    transform: scaleX(0.78);
    transform-origin: left center;
  }
  .contact .info-line { left: 93px; }
  .icon {
    position: absolute;
    left: 62px;
    width: 24px;
    height: 24px;
    fill: var(--neon-green);
  }
  .hours-title {
    position: absolute;
    left: 676px;
    width: 272px;
    top: 260px;
    margin: 0;
    text-align: center;
    font-family: "PT Sans Narrow", sans-serif;
    font-weight: 400;
    font-size: 44px;
    line-height: 1;
    color: var(--neon-green);
  }
  .hours .day { left: 576px; }
  .hours .time {
    right: 72px;
    transform-origin: right center;
  }
  .footer {
    position: absolute;
    left: 0; bottom: 0;
    width: 1108px;
    height: 90px;
  }
</style>
</head>
<body>
  <div class="card">
    <div class="header-band"></div>
    <div class="header-rule"></div>
    <div class="title-box">
      <h1 class="title">Mel’s Apothecary Owner/Pharm D.</h1>
    </div>

    <div class="contact">
      <svg class="icon" style="top:273px" viewBox="0 0 24 24" aria-hidden="true">
        <path d="M12 2 1 12h3v10h6v-6h4v6h6V12h3z"/>
      </svg>
      <p class="info-line" style="top:264px">7134 North Brook Lane</p>
      <p class="info-line" style="top:358px">Sioux Falls, SD 57231</p>

      <svg class="icon" style="top:462px" viewBox="0 0 24 24" aria-hidden="true">
        <path d="M2 9c0-4 20-4 20 0v2h-5V8H7v3H2zM6 12l2-3h8l2 3v9H6zm6 2a3 3 0 1 0 0 6 3 3 0 0 0 0-6zm0 2a1 1 0 1 1 0 2 1 1 0 0 1 0-2z"/>
      </svg>
      <p class="info-line" style="top:452px">605-318-6207</p>

      <svg class="icon" style="top:546px" viewBox="0 0 24 24" aria-hidden="true">
        <path d="M2 8c0-4 20-4 20 0v2h-5V7H7v3H2zM6 11l2-2h8l2 2v11H6zm3 3v2h2v-2zm4 0v2h2v-2zm-4 3v2h2v-2zm4 0v2h2v-2z"/>
      </svg>
      <p class="info-line" style="top:536px">605-318-6209</p>
    </div>

    <div class="hours">
      <h2 class="hours-title">Store hours</h2>
      <p class="info-line day" style="top:358px">Monday-Friday</p>
      <p class="info-line time" style="top:358px">8 am - 7 pm</p>
      <p class="info-line day" style="top:446px">Saturday</p>
      <p class="info-line time" style="top:446px">8 am - 12 pm</p>
      <p class="info-line day" style="top:526px">Sunday</p>
      <p class="info-line time" style="top:526px">Closed</p>
    </div>

    <svg class="footer" viewBox="0 0 1108 90" aria-hidden="true">
      <polygon points="0,0 734,0 744,15 0,15" fill="var(--silver)"/>
      <polygon points="0,15 797,15 849,90 0,90" fill="var(--neon-green)"/>
      <polygon points="824,15 1108,15 1108,90 874,90" fill="var(--silver)"/>
    </svg>
  </div>
</body>
</html>
```